Travonex web site / landing page

Looking for design help with building a landing page for our company and possible the remaining site. We are an AI developer and customer software developer company. Uploading logos for color scheme attached in logo xip file.

Target Market(s)

Manufacturing, Small business, Sales

Coding

Coded - Design and coding required

Number of Pages Required

3 page

Colors

Designer to choose colors to be used in the design.

Requirements
Must have
• Landing page, additional pages for AI, Custom software and Customer Portals explanation.

```html
<!DOCTYPE html>
<html lang="en">
<head>
<meta charset="utf-8">
<title>Travonex — AI &amp; Customer Software Developer</title>
<link rel="stylesheet" href="https://fonts.googleapis.com/css2?family=Lato:wght@400;700&family=Tinos&display=swap">
<style>
:root{
  --blue:#1b7dc5;
  --blue-deep:#0c4a80;
  --blue-dark:#0f5a9a;
  --sky:#6fcdf0;
  --sky-pale:#e9f4fc;
  --ink:#333b44;
  --text:#4a5560;
  --white:#ffffff;
}
*{box-sizing:border-box;margin:0;padding:0}
html,body{width:1200px;height:3047px;overflow:hidden}
body{position:relative;background:var(--white);font-family:"Lato",sans-serif;color:var(--text)}
.abs{position:absolute}
.serif{font-family:"Tinos",serif;font-weight:400}
.bg-art{position:absolute;left:0;top:0}
/* header */
.brand{left:142px;top:28px;display:flex;align-items:center;gap:10px;color:var(--white);font-size:14px;letter-spacing:5px}
.brand-dot{width:26px;height:26px;border-radius:50%;background:var(--white)}
.nav{top:24px;left:675px;font-size:13px;color:var(--ink)}
.nav a{color:var(--ink);text-decoration:none;position:absolute;white-space:nowrap;top:8px}
.nav .contact{left:286px;top:0;width:96px;height:30px;border-radius:15px;background:var(--sky);display:flex;align-items:center;justify-content:center;box-shadow:0 3px 6px rgba(0,0,0,.2)}
/* hero */
.hero-kicker{left:142px;top:163px;color:var(--white);font-size:14px}
.hero-title{left:142px;top:183px;color:var(--white);font-size:26px;line-height:32px;text-transform:uppercase;white-space:nowrap}
.btn{display:flex;align-items:center;justify-content:center;border-radius:16px;font-size:13px;text-transform:uppercase;box-shadow:0 4px 8px rgba(0,0,0,.22)}
.btn-sky{background:var(--sky);color:var(--blue-deep);border:1px solid var(--white)}
.btn-line{background:var(--blue);color:var(--white);border:1px solid var(--white)}
.btn-solid{background:var(--blue);color:var(--white)}
/* services */
.card{position:absolute;width:239px;height:240px;background:var(--white);border-radius:10px;box-shadow:0 6px 24px rgba(40,90,140,.12);padding:24px 20px}
.card.active{background:linear-gradient(160deg,#7dd3f3,#5fc2ec)}
.card h3{font-size:16px;font-weight:700;color:var(--ink);line-height:20px;margin:16px 0 12px;text-transform:uppercase}
.card.active h3{color:var(--blue-deep)}
.card p{font-size:12.5px;line-height:20px}
.card.active p{color:var(--blue-deep)}
.card svg{display:block}
.kicker{font-size:14px;color:var(--blue)}
.sec-title{font-size:24px;line-height:25px;color:var(--ink);text-transform:uppercase;white-space:nowrap}
.sec-title span{color:var(--blue)}
.sec-rule{height:1px;background:#c9ced3}
.body-copy{font-size:12.5px;line-height:28px;color:var(--text)}
/* testimonials */
.avatar{position:absolute;border-radius:50%;border:1px solid #b8bec4;padding:3px}
.avatar i{display:block;width:100%;height:100%;border-radius:50%;background:linear-gradient(#e2e4e6,#c8ccd0)}
.avatar.main{border-color:var(--blue)}
.avatar.main i{background:linear-gradient(#cfe4f4,#8fb6d6)}
.quote-text{left:330px;top:2114px;width:540px;text-align:center;font-size:12.5px;line-height:28px}
.quote-name{left:400px;top:2236px;width:400px;text-align:center;font-size:15px;color:var(--ink)}
.quote-name b{color:var(--blue-dark)}
.dots{left:550px;top:2285px;display:flex;gap:8px;align-items:center}
.dots i{width:12px;height:12px;border-radius:50%;background:#c9cdd1}
.dots i.on{width:18px;height:18px;background:var(--blue-deep)}
/* footer */
.news-title{left:195px;top:2612px;font-size:17px;color:var(--white)}
.news-sub{left:421px;top:2600px;font-size:12.5px;line-height:20px;color:var(--white)}
.news-form{left:650px;top:2606px;width:350px;height:32px;border-radius:16px;background:var(--sky);border:1px solid var(--white);display:flex;align-items:center;font-size:11px;color:var(--blue-deep);padding-left:14px;gap:10px}
.news-form .subscribe{position:absolute;right:-1px;top:-1px;width:118px;height:32px;border-radius:16px;background:var(--blue);color:var(--white);font-size:13px;display:flex;align-items:center;justify-content:center;border:1px solid var(--white)}
.foot-h{font-size:17px;color:var(--white);text-transform:uppercase;top:2724px}
.foot-list{list-style:none;font-size:13px;color:var(--white);text-transform:uppercase}
.foot-list li{height:38px;position:relative;padding-left:12px}
.foot-list li::before{content:"";position:absolute;left:0;top:6px;width:5px;height:5px;border-radius:50%;background:currentColor}
.foot-list li.current{color:var(--sky);font-weight:700}
.contact-row{position:absolute;left:322px;display:flex;gap:14px;align-items:center;color:var(--white);font-size:12.5px;line-height:18px}
.contact-icon{width:32px;height:32px;border-radius:50%;background:var(--sky);display:flex;align-items:center;justify-content:center;flex:none}
.foot-rule{left:141px;top:2979px;width:918px;height:1px;background:#2e6aa1}
.copyright{left:141px;top:3006px;font-size:12.5px;color:var(--white)}
.social{top:3001px;left:927px;display:flex;gap:9px}
.social i{width:26px;height:26px;border-radius:50%;border:1.5px solid var(--sky)}
</style>
</head>
<body>

<svg class="bg-art" width="1200" height="600" viewBox="0 0 1200 600" aria-hidden="true">
  <defs>
    <linearGradient id="photoTone" x1="0" y1="0" x2="1" y2="1">
      <stop offset="0" stop-color="#b9e7f8"/><stop offset=".6" stop-color="#7ccfef"/><stop offset="1" stop-color="#4fb8e6"/>
    </linearGradient>
  </defs>
  <path d="M0 0H1200V420C1120 520 980 585 820 580C620 572 470 470 300 462C180 457 80 480 0 520Z" fill="#6fcdf0"/>
  <path d="M0 0H1200V405C1110 505 980 568 820 563C620 556 470 455 300 447C180 442 80 465 0 500Z" fill="#1b7dc5"/>
</svg>

<svg class="abs" style="left:580px;top:0" width="620" height="560" viewBox="580 0 620 560" role="img" aria-label="Photo of three colleagues working together at a laptop">
  <path d="M655 0H1200V400C1120 510 980 555 850 545C700 533 588 430 590 290C592 160 625 70 655 0Z" fill="none" stroke="#0f5a9a" stroke-width="10"/>
  <path d="M655 0H1200V400C1120 510 980 555 850 545C700 533 588 430 590 290C592 160 625 70 655 0Z" fill="url(#photoTone)"/>
  <circle cx="670" cy="440" r="26" fill="#0f5a9a"/>
  <circle cx="1076" cy="512" r="17" fill="#0f5a9a"/>
</svg>

<div class="abs brand"><span class="brand-dot"></span>TRAVONEX</div>
<nav class="abs nav">
  <a href="#" style="left:0">HOME</a>
  <a href="#" style="left:81px">ABOUT US</a>
  <a href="#" style="left:187px">SERVICES</a>
  <a href="#" class="contact">CONTACT</a>
</nav>

<div class="abs hero-kicker">We’re The Best</div>
<h1 class="abs hero-title serif">AI &amp; Customer Software<br>Developer Company<br>In The World</h1>
<a class="abs btn btn-sky" style="left:142px;top:291px;width:117px;height:31px">Get Started</a>
<a class="abs btn btn-line" style="left:266px;top:291px;width:117px;height:31px">Learn More</a>

<svg class="abs" style="left:0;top:600px" width="620" height="680" aria-hidden="true">
  <circle cx="100" cy="210" r="210" fill="#eaf5fc"/>
  <circle cx="290" cy="420" r="150" fill="#eaf5fc"/>
  <circle cx="500" cy="215" r="110" fill="#eef6fd"/>
</svg>
<article class="card" style="left:141px;top:709px">
  <svg width="56" height="56" viewBox="0 0 56 56" fill="none" stroke="#1b5f9e" stroke-width="2"><path d="M27 6C14 6 8 14 8 24s6 18 19 22V6z"/><path d="M29 6c13 0 19 8 19 18s-6 18-19 22V6z"/><circle cx="18" cy="20" r="3"/><circle cx="38" cy="30" r="3"/></svg>
  <h3>AI Custom<br>Software</h3>
  <p>Lorem ipsum dolor sit amet, conse ctetuer adipiscing elit, sed diam nonummy nibh euismod.</p>
</article>
<article class="card" style="left:141px;top:969px">
  <svg width="56" height="56" viewBox="0 0 56 56" fill="none" stroke="#1b5f9e" stroke-width="2"><rect x="4" y="10" width="48" height="32" rx="2"/><path d="M20 50h16M28 42v8"/><rect x="10" y="4" width="14" height="14" rx="2"/><path d="M17 8v6"/></svg>
  <h3>Customer Portals<br>Explanation</h3>
  <p>Lorem ipsum dolor sit amet, conse ctetuer adipiscing elit, sed diam nonummy nibh euismod.</p>
</article>
<article class="card active" style="left:401px;top:863px">
  <svg width="56" height="56" viewBox="0 0 56 56" fill="none" stroke="#0c4a80" stroke-width="2"><rect x="4" y="12" width="48" height="32" rx="2"/><path d="M20 52h16M28 44v8"/><circle cx="28" cy="10" r="6"/></svg>
  <h3>Custom<br>Software</h3>
  <p>Lorem ipsum dolor sit amet, conse ctetuer adipiscing elit, sed diam nonummy nibh euismod.</p>
</article>

<div class="abs kicker" style="left:703px;top:812px">We’re Offering</div>
<div class="abs sec-rule" style="left:703px;top:833px;width:355px"></div>
<h2 class="abs sec-title serif" style="left:701px;top:838px">Travonex <span>Custom Services</span></h2>
<p class="abs body-copy" style="left:703px;top:889px;width:360px">Lorem ipsum dolor sit amet, consectetuer adipiscing elit, sed diam nonummy nibh euismod tincidunt ut laoreet dolore magna aliquam erat volutpat. Ut wisi enim ad minim veniam, quis nostrud exerci tation ullamcorper suscipit lobortis nisl ut aliquip ex ea commodo consequat.</p>
<a class="abs btn btn-solid" style="left:704px;top:1061px;width:116px;height:30px">Learn More</a>

<div class="abs kicker" style="left:175px;top:1371px">About Us</div>
<div class="abs sec-rule" style="left:175px;top:1392px;width:355px"></div>
<h2 class="abs sec-title serif" style="left:174px;top:1395px">Travonex <span>Software<br>Developer Team</span></h2>
<p class="abs body-copy" style="left:175px;top:1473px;width:360px">Lorem ipsum dolor sit amet, consectetuer adipiscing elit, sed diam nonummy nibh euismod tincidunt ut laoreet dolore magna aliquam erat volutpat. Ut wisi enim ad minim veniam, quis nostrud exerci tation ullamcorper suscipit lobortis nisl ut aliquip ex ea commodo consequat.</p>
<a class="abs btn btn-solid" style="left:176px;top:1646px;width:116px;height:30px">Learn More</a>

<svg class="abs" style="left:430px;top:1320px" width="700" height="560" aria-hidden="true">
  <defs>
    <radialGradient id="softGrey" cx=".5" cy=".5" r=".5">
      <stop offset="0" stop-color="#f1f2f3"/><stop offset="1" stop-color="#ffffff" stop-opacity="0"/>
    </radialGradient>
  </defs>
  <ellipse cx="190" cy="380" rx="170" ry="170" fill="url(#softGrey)"/>
  <path d="M210 60 Q215 30 245 25 L545 20 Q575 18 590 50 L640 240 Q650 280 615 295 L290 375 Q255 384 240 355 L195 205 Q190 190 198 170 Z" fill="#1b7dc5"/>
</svg>
<svg class="abs" style="left:648px;top:1361px" width="411" height="319" role="img" aria-label="Photo of a development team gathered around a laptop">
  <rect width="411" height="319" rx="40" fill="#cdd8e0"/>
</svg>

<svg class="abs" style="left:414px;top:1923px" width="154" height="124" aria-hidden="true">
  <path d="M0 124V58C0 22 20 4 66 0V26C44 30 36 40 36 58H74V124Z M80 124V58C80 22 100 4 146 0V26C124 30 116 40 116 58H154V124Z" fill="#eaf5fc"/>
</svg>
<div class="avatar" style="left:209px;top:1873px;width:52px;height:52px" role="img" aria-label="Client portrait"><i></i></div>
<div class="avatar" style="left:411px;top:1857px;width:68px;height:68px" role="img" aria-label="Client portrait"><i></i></div>
<div class="avatar" style="left:903px;top:1849px;width:68px;height:68px" role="img" aria-label="Client portrait"><i></i></div>
<div class="avatar" style="left:805px;top:1996px;width:68px;height:68px" role="img" aria-label="Client portrait"><i></i></div>
<div class="avatar" style="left:232px;top:2082px;width:68px;height:68px" role="img" aria-label="Client portrait"><i></i></div>
<div class="avatar" style="left:880px;top:2201px;width:52px;height:52px" role="img" aria-label="Client portrait"><i></i></div>
<div class="avatar main" style="left:544px;top:1974px;width:112px;height:112px" role="img" aria-label="Portrait of the featured client"><i></i></div>
<p class="abs quote-text">Lorem ipsum dolor sit amet, consectetuer adipiscing elit, sed diam nonummy nibh euismod tincidunt ut laoreet dolore magna aliquam erat volutpat. Ut wisi enim ad minim veniam, quis nostrud exerci tation ullamcorper suscipit lobortis nisl ut aliquip</p>
<div class="abs quote-name"><b>LOREM IPSUM,</b> wisi enim</div>
<div class="abs dots"><i></i><i></i><i class="on"></i><i></i><i></i></div>

<svg class="abs" style="left:0;top:2400px" width="1200" height="647" aria-hidden="true">
  <path d="M0 190C120 40 330 10 560 30C800 50 1000 170 1200 70V647H0Z" fill="#6fcdf0"/>
  <path d="M0 195C120 55 330 25 560 45C800 65 1000 190 1200 95V647H0Z" fill="#0c4a80"/>
  <line x1="405" y1="180" x2="405" y2="245" stroke="#2e6aa1"/>
  <line x1="632" y1="180" x2="632" y2="245" stroke="#2e6aa1"/>
  <circle cx="974" cy="410" r="82" fill="none" stroke="#3e7db2" stroke-width="3"/>
</svg>
<div class="abs news-title serif">NEWSLETTER SIGN UP</div>
<div class="abs news-sub">Subscribe to our newsletter to get<br>the latest update to your inbox</div>
<div class="abs news-form">
  <svg width="14" height="14" viewBox="0 0 14 14"><path d="M1 7L13 1L9 13L7 8Z" fill="#0c4a80"/></svg>
  Enter your email address
  <span class="subscribe">SUBSCRIBE</span>
</div>

<h4 class="abs foot-h serif" style="left:141px">Quick Links</h4>
<h4 class="abs foot-h serif" style="left:322px">Contact Details</h4>
<h4 class="abs foot-h serif" style="left:587px">Our Services</h4>
<ul class="abs foot-list" style="left:141px;top:2767px">
  <li class="current">Home</li><li>About Us</li><li>Services</li><li>Contact</li>
</ul>
<ul class="abs foot-list" style="left:587px;top:2767px">
  <li>AI Custom Software</li><li>Custom Software</li><li>Customer Portals Explanation</li>
</ul>
<div class="contact-row" style="top:2766px">
  <span class="contact-icon"><svg width="14" height="18" viewBox="0 0 14 18"><path d="M7 1a6 6 0 0 1 6 6c0 4-6 10-6 10S1 11 1 7a6 6 0 0 1 6-6z" fill="#0c4a80"/><circle cx="7" cy="7" r="2.2" fill="#6fcdf0"/></svg></span>
  <span>48, Maple Grove Avenue,<br>Unit 7, RIVERTON 20418</span>
</div>
<div class="contact-row" style="top:2814px">
  <span class="contact-icon"><svg width="16" height="16" viewBox="0 0 16 16"><path d="M3 1l3 3-2 2c1 2 3 4 5 5l2-2 3 3-2 3C7 15 1 9 1 3z" fill="#0c4a80"/></svg></span>
  <span>CALL US:<br>+1 555 010 2468</span>
</div>
<div class="contact-row" style="top:2861px">
  <span class="contact-icon"><svg width="16" height="16" viewBox="0 0 14 14"><path d="M1 7L13 1L9 13L7 8Z" fill="#0c4a80"/></svg></span>
  <span>EMAIL US:<br>info@travonex.com</span>
</div>

<div class="abs foot-rule"></div>
<div class="abs copyright">Copyright © 2019 TRAVONEX. All Rights Reserved.</div>
<div class="abs social"><i></i><i></i><i></i><i></i></div>

</body>
</html>
```